Paraffin Wax Packaging Design for Nail and Beauty Industry

We need an attractive design for the packaging of our new product, Paraffin Wax. Our company is a wholesale beauty/nail supply company that has been selling to nail salons in the US market for 10 years. We currently sell this product that we buy from another company. Now we want to launch our own brand of Paraffin Wax.

Target Market(s)

Retail nail salons in the US market.

Industry/Entity Type

Industry

Font styles to use
Sans Serif

Colors

Designer to choose colors to be used in the design.

Requirements
Must have
• Our logo (attached).
• All information on the "Ingredient List" (attached).
• Design for Clear Packaging so product can show through.
• Design for Package Dimensions of 4.25" x 11" (110cm x 280 cm).
Nice to have
• Picture related to women's skin and or beauty.
• Contrast as in the design of product that we currently sell (attached).

```html
<!DOCTYPE html>
<html lang="en">
<head>
<meta charset="utf-8">
<title>Antibacterial Paraffin Wax – Packaging</title>
<link rel="stylesheet" href="https://fonts.googleapis.com/css2?family=Abril+Fatface&family=Caveat+Brush&family=Montserrat:wght@500;600;700&family=Open+Sans:ital,wght@1,400&family=Playfair+Display:wght@400&family=Roboto:wght@500;700;900&display=swap">
<style>
  :root {
    --lilac: #dcc4e0;
    --navy: #302a7a;
    --blue: #1f6cb8;
    --white: #ffffff;
    --label-red: #8b1f0f;
    --photo-light: #f3dcd0;
    --photo-mid: #d9a88e;
  }
  html, body { margin: 0; padding: 0; overflow: hidden; }
  body { width: 738px; height: 1200px; background: var(--lilac); position: relative; font-family: "Montserrat", sans-serif; }
  .abs { position: absolute; }

  .package { position: absolute; left: 170px; top: 94px; width: 397px; height: 1010px; }

  .top-band { left: 0; top: 0; width: 397px; height: 142px; background: var(--navy); border-radius: 18px 18px 0 0; border-top: 6px solid var(--blue); box-sizing: border-box; }
  .brand-box { left: 90px; top: 20px; width: 218px; height: 67px; background: var(--white); border-radius: 8px; display: flex; align-items: center; justify-content: center; }
  .brand-name { font-family: "Montserrat", sans-serif; font-weight: 600; font-size: 26px; color: var(--navy); }
  .ornament { left: 58px; top: 106px; width: 282px; height: 72px; background: linear-gradient(180deg, rgba(31,108,184,0.35), rgba(31,108,184,0.05)); border-radius: 0 0 60px 60px; }

  .title-frame { left: 20px; top: 210px; width: 360px; height: 110px; }
  .title-sub { left: 0; width: 397px; top: 206px; text-align: center; font-family: "Playfair Display", serif; font-size: 27px; line-height: 34px; color: var(--navy); }
  .title-main { left: 0; width: 397px; top: 232px; text-align: center; font-family: "Abril Fatface", serif; font-size: 78px; line-height: 1; color: var(--navy); }
  .title-wax { left: 212px; top: 292px; font-family: "Caveat Brush", cursive; font-size: 100px; line-height: 1; color: var(--navy); }

  .compat-icon { left: 176px; top: 396px; width: 44px; height: 44px; }
  .compat-title { left: 0; width: 397px; top: 438px; text-align: center; font-weight: 600; font-size: 21px; line-height: 24px; color: var(--navy); }
  .compat-band { left: 0; top: 461px; width: 397px; height: 19px; background: var(--navy); color: var(--white); font-weight: 500; font-size: 14px; line-height: 19px; text-align: center; }

  .photo { left: 0; top: 598px; width: 397px; height: 256px; background: radial-gradient(ellipse at 68% 45%, var(--photo-light) 0%, var(--photo-mid) 55%, rgba(217,168,142,0) 80%); }
  .claim { left: 0; top: 544px; width: 270px; color: var(--navy); text-align: center; }
  .claim-small { font-weight: 600; font-size: 15px; line-height: 1.2; display: block; }
  .claim-big { font-family: "Caveat Brush", cursive; font-size: 52px; line-height: 0.85; display: block; }
  .claim .deeply { font-size: 17px; font-weight: 500; }

  .bottom-wave { left: 0; top: 842px; width: 397px; height: 30px; }
  .bottom-panel { left: 0; top: 866px; width: 397px; height: 144px; background: var(--navy); border-radius: 0 0 18px 18px; }
  .caution-title { left: 16px; top: 893px; font-family: "Roboto", sans-serif; font-weight: 900; font-size: 13px; line-height: 15px; color: var(--white); }
  .caution-box { left: 16px; top: 914px; width: 163px; height: 44px; border: 2px solid var(--white); border-left: none; box-sizing: border-box; display: flex; align-items: center; color: var(--white); font-family: "Roboto", sans-serif; }
  .caution-box svg { flex: none; margin: 0 6px 0 2px; }
  .caution-text { text-align: center; line-height: 1.1; }
  .caution-text strong { font-size: 9.5px; font-weight: 700; display: block; }
  .caution-text span { font-size: 7px; font-weight: 700; display: block; }
  .net-wt { left: 16px; top: 985px; padding: 2px 4px; line-height: 14px; background: var(--white); color: var(--navy); font-family: "Roboto", sans-serif; font-weight: 700; font-size: 11px; border-radius: 2px; }

  .ingredients-head { left: 253px; top: 890px; width: 137px; height: 20px; background: var(--white); color: var(--navy); font-family: "Roboto", sans-serif; font-weight: 900; font-size: 13px; line-height: 20px; text-align: center; letter-spacing: 0.5px; border-radius: 3px; }
  .ingredients-list { left: 253px; top: 912px; margin: 0; padding: 0; list-style: none; color: var(--white); font-family: "Open Sans", sans-serif; font-style: italic; font-size: 11px; }
  .ingredients-list li { height: 15.4px; line-height: 15.4px; white-space: nowrap; }
  .ingredients-list li::before { content: "\2733"; display: inline-block; line-height: 1; vertical-align: middle; font-style: normal; font-size: 8px; margin-right: 6px; }

  .clear-note { left: 600px; top: 600px; width: 114px; text-align: right; color: var(--label-red); font-weight: 600; font-size: 18px; line-height: 22px; }
  .clear-arrow { left: 524px; top: 632px; width: 92px; height: 12px; }
</style>
</head>
<body>
  <div class="package">
    <div class="abs top-band"></div>
    <div class="abs brand-box"><span class="brand-name">By Solena</span></div>
    <div class="abs ornament" role="img" aria-label="Decorative blue scroll ornament"></div>

    <svg class="abs title-frame" viewBox="0 0 360 110" aria-hidden="true">
      <path d="M90 18 H28 C4 18 2 44 2 55 C2 85 20 102 60 104 H200" fill="none" stroke="var(--navy)" stroke-width="2"/>
      <path d="M270 18 H330 C354 18 358 44 358 55 C358 70 352 80 340 86" fill="none" stroke="var(--navy)" stroke-width="2"/>
    </svg>
    <div class="abs title-sub">Antibacterial</div>
    <div class="abs title-main">Paraffin</div>
    <div class="abs title-wax">WAX</div>

    <svg class="abs compat-icon" viewBox="0 0 44 44" aria-hidden="true">
      <circle cx="22" cy="22" r="19" fill="none" stroke="var(--navy)" stroke-width="4"/>
      <path d="M12 22 L20 30 L38 8" fill="none" stroke="var(--navy)" stroke-width="5" stroke-linecap="round" stroke-linejoin="round"/>
    </svg>
    <div class="abs compat-title">COMPATIBLE</div>
    <div class="abs compat-band">for use with most wax paraffin heat therapy units.</div>

    <div class="abs photo" role="img" aria-label="Photo of a smiling woman with a towel on her hair resting on her arms"></div>
    <div class="abs claim">
      <span class="claim-small deeply">Deeply</span>
      <span class="claim-big">Moisturizes</span>
      <span class="claim-small">the Skin Restoring a</span>
      <span class="claim-big">Healthier</span>
      <span class="claim-small">Look and Feel to Skin.</span>
    </div>

    <svg class="abs bottom-wave" viewBox="0 0 397 30" preserveAspectRatio="none" aria-hidden="true">
      <path d="M0 8 C120 22 280 22 397 8 V30 H0 Z" fill="var(--blue)"/>
      <path d="M0 18 C120 30 280 30 397 18 V30 H0 Z" fill="var(--navy)"/>
    </svg>
    <div class="abs bottom-panel"></div>

    <div class="abs caution-title">CAUTION:</div>
    <div class="abs caution-box">
      <svg width="22" height="22" viewBox="0 0 22 22" aria-hidden="true">
        <circle cx="11" cy="11" r="9.5" fill="none" stroke="var(--white)" stroke-width="2"/>
        <path d="M11 5 C13 8 15 10 15 13 A4 4 0 0 1 7 13 C7 11 8 10 9 9 C9 11 10 12 11 12 C10 9 11 7 11 5 Z" fill="var(--white)"/>
      </svg>
      <div class="caution-text">
        <strong>PARAFFIN IS FLAMMABLE.</strong>
        <span>Do not use near open flame or an<br>unprotected resistance heater.</span>
      </div>
    </div>
    <div class="abs net-wt">Net Wt. 1 lb. (450 g.)</div>

    <div class="abs ingredients-head">INGREDIENTS</div>
    <ul class="abs ingredients-list">
      <li>Paraffin waxes</li>
      <li>Hydrocarbon waxes</li>
      <li>Petrolatum</li>
      <li>Paraffin oils</li>
      <li>Apricot kernel oil</li>
      <li>Fragrance D &amp; C dyes.</li>
    </ul>
  </div>

  <div class="abs clear-note">Clear<br>Packaging</div>
  <svg class="abs clear-arrow" viewBox="0 0 92 12" aria-hidden="true">
    <line x1="10" y1="6" x2="92" y2="6" stroke="var(--label-red)" stroke-width="2"/>
    <path d="M0 6 L14 2 L14 10 Z" fill="var(--label-red)"/>
  </svg>
</body>
</html>
```